Brightfield Optics seeks updated contemporary business card

Brightfield Optics utilizes advanced technology and we take pride in the modern look and feel of our practice. We like our current card, but it's been four years so it is time for an update.

Target Market(s)

Females 25-45 make the most health care decisions for their family.

Contact Information for Business Card

Clean front. Back with info and with empty space for appointment time or other small note

Requirements
Must have
• Logo
Meadow Costmart, 24816 E Tamsworth Ave
Pinecrest Costmart, 3084 S Dunmore Rd
Call or text: 509-482-6134
email: hello@brightfieldoptics.example
brightfieldoptics.example
Dr Tomas Bregan & Associates

```html
<!DOCTYPE html>
<html lang="en">
<head>
<meta charset="utf-8">
<title>Brightfield Optics – Business Card</title>
<link href="https://fonts.googleapis.com/css2?family=Questrial&display=swap" rel="stylesheet">
<style>
  :root {
    --navy: #2c3d67;
    --blue: #259bd8;
    --white: #ffffff;
    --stage-center: #1c5a7d;
    --stage-edge: #2c3d67;
  }
  * { margin: 0; padding: 0; box-sizing: border-box; }
  html, body { width: 1200px; height: 732px; overflow: hidden; }
  body {
    background: radial-gradient(ellipse at 50% 50%, var(--stage-center) 0%, #215679 45%, var(--stage-edge) 100%);
    font-family: "Questrial", sans-serif;
    color: var(--navy);
    position: relative;
  }
  .card {
    position: absolute;
    top: 222px;
    width: 504px;
    height: 288px;
    background: var(--white);
    overflow: hidden;
  }
  .card--info { left: 90px; }
  .card--front { left: 606px; }
  .card__shapes { position: absolute; inset: 0; width: 100%; height: 100%; }

  .brand {
    position: absolute;
    display: flex;
    align-items: center;
    gap: 8px;
    color: var(--navy);
    white-space: nowrap;
  }
  .brand__dot { border-radius: 50%; background: var(--blue); flex: none; }
  .card--info .brand { left: 14px; top: 56px; font-size: 24px; }
  .card--info .brand__dot { width: 16px; height: 16px; }
  .card--front .brand { left: 0; right: 0; top: 126px; justify-content: center; font-size: 36px; }
  .card--front .brand__dot { width: 24px; height: 24px; }

  .practice {
    position: absolute;
    left: 11px;
    top: 132px;
    font-size: 22px;
    letter-spacing: -0.2px;
  }
  .contact {
    position: absolute;
    left: 11px;
    top: 181px;
    list-style: none;
    font-size: 12.5px;
    line-height: 1.35;
  }
  .contact li.gap { margin-top: 4px; }
</style>
</head>
<body>
  <section class="card card--info" aria-label="Card back with contact details">
    <svg class="card__shapes" viewBox="0 0 504 288" aria-hidden="true">
      <path d="M452,0 C462,150 392,240 276,288 L504,288 L504,0 Z" fill="var(--navy)"/>
      <path d="M464,0 C474,150 414,240 288,288 L504,288 L504,0 Z" fill="var(--blue)"/>
    </svg>
    <div class="brand"><span class="brand__dot"></span>Brightfield Optics</div>
    <h1 class="practice">Dr Tomas Bregan &amp; Associates</h1>
    <ul class="contact">
      <li>Meadow Costmart, 24816 E Tamsworth Ave</li>
      <li>Pinecrest Costmart, 3084 S Dunmore Rd</li>
      <li class="gap">Call or text: 509-482-6134</li>
      <li class="gap">email: hello@brightfieldoptics.example</li>
      <li class="gap">brightfieldoptics.example</li>
    </ul>
  </section>

  <section class="card card--front" aria-label="Card front">
    <svg class="card__shapes" viewBox="0 0 504 288" aria-hidden="true">
      <path d="M0,0 L168,0 C80,16 16,90 0,195 Z" fill="var(--navy)"/>
      <path d="M504,95 C490,200 430,276 334,288 L504,288 Z" fill="var(--blue)"/>
    </svg>
    <div class="brand"><span class="brand__dot"></span>Brightfield Optics</div>
  </section>
</body>
</html>
```